Business card design

I have a PDF of just what I want, but I need it to be digitized for Tandor Cards so I can edit and modify for new employees and reorder going forward

```html
<!DOCTYPE html>
<html lang="en">
<head>
<meta charset="utf-8">
<title>Nova Property Managers – Business Cards</title>
<link href="https://fonts.googleapis.com/css2?family=Source+Sans+3:wght@400;600;700&display=swap" rel="stylesheet">
<style>
  :root {
    --sheet: #ffffff;
    --card-blue: #2495d6;
    --band-black: #0a0a0a;
    --ink-white: #ffffff;
    --ink-dark: #0b0b0b;
    --skyline-dark: #101418;
    --crop: #6b6b6b;
  }
  * { margin: 0; padding: 0; box-sizing: border-box; }
  html, body {
    width: 1200px; height: 778px; overflow: hidden;
    background: var(--sheet);
    font-family: "Source Sans 3", "Myriad Pro", Arial, sans-serif;
  }
  .sheet { position: relative; width: 1200px; height: 778px; }
  .crop-marks { position: absolute; inset: 0; }
  .card {
    position: absolute; top: 47px;
    width: 488px; height: 688px;
    background: var(--card-blue);
    color: var(--ink-white);
    text-align: center;
    overflow: hidden;
  }
  .card--left { left: 86px; }
  .card--right { left: 647px; }
  .brand-band {
    position: absolute; top: 57px; left: 0; right: 0; height: 94px;
    background: var(--band-black);
    font-weight: 700;
    color: var(--ink-white);
  }
  .brand-name {
    position: absolute; top: 2px; left: 0; right: 0;
    font-size: 54px; line-height: 60px; letter-spacing: 2px;
  }
  .brand-tagline {
    position: absolute; top: 58px; left: 0; right: 0;
    font-size: 25px; line-height: 28px; letter-spacing: 0.5px;
  }
  .person {
    position: absolute; top: 198px; left: 0; right: 0;
    color: var(--ink-white);
  }
  .person-name { font-size: 31px; font-weight: 400; line-height: 38px; }
  .person-role,
  .person-mobile { font-size: 21px; font-weight: 600; line-height: 29px; color: var(--ink-dark); }
  .person-role { color: var(--ink-white); }
  .contact {
    position: absolute; top: 363px; left: 0; right: 0;
    list-style: none;
    font-size: 21px; font-weight: 600; line-height: 29px;
    color: var(--ink-white);
  }
  .contact .spacer { height: 12px; }
  .skyline {
    position: absolute; left: 26px; right: 41px; top: 560px; height: 92px;
    background: linear-gradient(to bottom, rgba(16,20,24,0.55), var(--skyline-dark) 55%);
  }
</style>
</head>
<body>
<main class="sheet">
  <svg class="crop-marks" width="1200" height="778" aria-hidden="true">
    <g stroke="var(--crop)" stroke-width="1.2">
      <line x1="86" y1="0" x2="86" y2="34"/><line x1="0" y1="47" x2="73" y2="47"/>
      <line x1="574" y1="0" x2="574" y2="34"/><line x1="587" y1="47" x2="612" y2="47"/>
      <line x1="86" y1="748" x2="86" y2="778"/><line x1="0" y1="735" x2="73" y2="735"/>
      <line x1="574" y1="748" x2="574" y2="778"/><line x1="587" y1="735" x2="612" y2="735"/>
      <line x1="647" y1="0" x2="647" y2="34"/><line x1="624" y1="47" x2="634" y2="47"/>
      <line x1="1135" y1="0" x2="1135" y2="34"/><line x1="1148" y1="47" x2="1200" y2="47"/>
      <line x1="647" y1="748" x2="647" y2="778"/><line x1="624" y1="735" x2="634" y2="735"/>
      <line x1="1135" y1="748" x2="1135" y2="778"/><line x1="1148" y1="735" x2="1200" y2="735"/>
    </g>
  </svg>

  <article class="card card--left">
    <header class="brand-band">
      <div class="brand-name">NOVA</div>
      <div class="brand-tagline">PROPERTY MANAGERS</div>
    </header>
    <section class="person">
      <h1 class="person-name">Marion Teller</h1>
      <p class="person-role">Director/ Manager</p>
      <p class="person-mobile">022 418 5561</p>
    </section>
    <ul class="contact">
      <li>G0, 24 Quay Lane,</li>
      <li>Harbourside, Auckland City</li>
      <li>Ph: (09) 472 1160</li>
      <li>Fax: (09) 472 1161</li>
      <li>Email: info@novarentals.co.nz</li>
      <li>www.novarentals.co.nz</li>
    </ul>
    <div class="skyline" role="img" aria-label="City skyline silhouette with harbour tower and a sailboat"></div>
  </article>

  <article class="card card--right">
    <header class="brand-band">
      <div class="brand-name">NOVA</div>
      <div class="brand-tagline">PROPERTY MANAGERS</div>
    </header>
    <section class="person">
      <h1 class="person-name">Owen Teller</h1>
      <p class="person-role">Director/ Manager</p>
      <p class="person-mobile">021 627 803</p>
    </section>
    <ul class="contact">
      <li>G0, 24 Quay Lane,</li>
      <li>Harbourside, Auckland City</li>
      <li>Ph: (09) 472 1160</li>
      <li>Fax: (09) 472 1161</li>
      <li>Email: info@novarentals.co.nz</li>
      <li>www.novarentals.co.nz</li>
    </ul>
    <div class="skyline" role="img" aria-label="City skyline silhouette with harbour tower and a sailboat"></div>
  </article>
</main>
</body>
</html>
```